Tallowmere Office Partners needs a new interactive and interesting website

We need an interesting, professional, modern and functional company website for Tallowmere Office Partners - a young IT Services company based out of Chennai, India.

Tallowmere Office Partners is a fully owned subsidiary of Hollin Cellarworks, one of the world's leading direct to consumer wine merchant.

We already have a registered company logo which must feature in the website.

We conceive, design, develop, test, implement and support IT solutions across the entire Hollin Cellarworks IT landscape. For ex : We currently run about 25 e-commerce websites for Hollin Cellarworks on KVM and Dot Net.

We would like to see our corporate colors used in the website. (Burgundy wine and wine green - source: www.tallowmereop.example)

We are looking at this website to communicate a fun, friendly and professionally managed company - reaching out to career seekers, prospective customers and general public.

For reference - The company name 'Tallowmere' is an inspiration from the Hollin Cellarworks lineage.

The second image with the world map is stickered on our main entrance to the office, I am not sure where this can be used -just putting it out there..
Updates

Please note that there are only a few more days to submit designs for this contest  !

I would appreciate if you can help posting your designs in time for our review and consideration.

Thanks.

Reason: Thanks for your inputs. We have a number of designers and a lot to digest and work with in the past few days. There has been a rush of new designs in the last few days Hence we will require more time to process these and make our decision. Hence i am requesting the contest to be open for more days. Regards, Suresh

Target Market(s)

Prospective job seekers who want to know more about the company and also wish to apply for a job vacancy
People wanting to know more about the company in general and our progress
People who want to see what we offer and how we can help them too - prospective customers
Companies that are interested in our IT Captive journey and are looking for a business opportunity

Industry/Entity Type

E-Commerce

Requirements
Must have
• Log In/ Register facility acting as a Single Sign on for Intranet (Employees)

Facility to post job vacancies (with an expiry date) and enable people to apply for a role and upload their CV/Resume.

Facility to Review Job applications

Facility for website visitors to contact Tallowmere Office Partners via an online 'Contact Us' form with a split of job seekers and business opportunities

Gallery facility to upload pictures regarding company events
Nice to have
• Less Cluttered and contemporary design
Some Wine/Vineyard inspirations will be good but not too much, the company is an IT services company

```html
<!DOCTYPE html>
<html lang="en">
<head>
<meta charset="utf-8">
<title>Tallowmere Office Partners</title>
<link rel="stylesheet" href="https://fonts.googleapis.com/css2?family=Source+Sans+3:wght@400;600;700&family=Arimo:wght@400&display=swap">
<style>
:root{
  --burgundy:#8a1446;
  --burgundy-dark:#6e0f37;
  --pink-line:#d6a4bc;
  --text:#333;
  --muted:#666;
  --rule:#e3e3e3;
  --hero-dark:#2a2a2a;
  --hero-mid:#4a4a4a;
  --white:#fff;
}
*{box-sizing:border-box;margin:0;padding:0}
html,body{width:993px;height:1200px;overflow:hidden;background:var(--white)}
body{position:relative;font-family:"Source Sans 3",Arial,sans-serif;color:var(--text)}
.abs{position:absolute}
a{color:inherit;text-decoration:none}

/* header */
.brand{left:124px;top:24px;display:flex;align-items:center;gap:8px}
.brand-mark{width:22px;height:22px;border-radius:50%;background:var(--burgundy)}
.brand-name{color:var(--burgundy);font-weight:700;font-size:22px;line-height:1.05;width:170px}
.account{right:124px;top:10px;display:flex;gap:8px;font-family:Arimo,Arial,sans-serif;font-size:9px;color:#222;align-items:center}
.account span.sep{color:#999}
.account .ico{display:inline-block;width:8px;height:8px;border-radius:50%;background:var(--burgundy);margin-right:4px;vertical-align:-1px}

/* nav */
.nav-rule{left:124px;width:745px;height:4px;border-top:1px solid var(--pink-line);border-bottom:2px solid var(--pink-line)}
.main-nav{left:124px;top:95px;width:745px;height:18px;display:flex;align-items:center;font-family:Arimo,Arial,sans-serif;font-size:9px;color:#222}
.main-nav a{margin-left:11px;margin-right:11px}
.main-nav a:first-child{margin-left:11px;color:var(--burgundy)}
.social{margin-left:auto;display:flex;gap:4px}
.social span{width:15px;height:15px;border-radius:50%;background:var(--burgundy)}

/* hero */
.hero{left:124px;top:130px;width:536px;height:333px;background:radial-gradient(ellipse at 45% 40%,var(--hero-mid),var(--hero-dark) 75%)}
.hero-title{left:226px;top:208px;color:var(--white);font-size:32px;font-weight:400;letter-spacing:.2px}
.hero-sub{left:226px;top:247px;width:330px;display:flex;align-items:center;gap:10px;color:#e5e5e5;font-size:15px}
.hero-sub i{flex:1;height:1px;background:#e5e5e5}
.action{width:100px;text-align:center;color:var(--white);font-size:12.5px;line-height:1.15}
.action .ring{width:46px;height:46px;margin:0 auto 8px;border:2px solid var(--white);border-radius:50%;display:flex;align-items:center;justify-content:center}
.action.active .ring{background:var(--burgundy)}
.action b{font-weight:600;display:block}
.photo{background:linear-gradient(135deg,#b9b9b9,#7d7f86)}

/* divider */
.divider{left:124px;top:478px;width:745px;height:4px;border-top:1px solid var(--pink-line);border-bottom:1px solid var(--pink-line)}
.divider-dot{left:490px;top:474px;width:12px;height:12px;border-radius:50%;background:var(--burgundy);border:3px solid var(--white);box-sizing:content-box}

/* welcome */
.welcome-title{left:0;width:993px;top:538px;text-align:center;font-size:20px;color:var(--burgundy)}
.welcome-title strong{font-weight:600}
.circle{top:589px;width:88px;height:88px;border-radius:50%}
.intro{left:165px;width:660px;top:705px;text-align:center;font-size:9.5px;line-height:1.42;color:#333}
.intro p{margin-bottom:11px}
.intro .lead{font-size:11.5px;font-weight:600;color:#222}
.intro .lead a{color:var(--burgundy)}

/* partners */
.band{left:124px;width:745px;height:1px;background:var(--rule)}
.partners{left:124px;width:745px;top:895px;display:flex;justify-content:space-around;align-items:center;font-size:14px;color:#8a8a8a;font-weight:400}

/* footer */
.col{top:1006px;font-size:8.5px;color:#222}
.col h3{font-size:11.5px;font-weight:400;color:var(--burgundy);margin-bottom:6px}
.col ul{list-style:none;margin-bottom:10px}
.col li{position:relative;padding-left:12px;line-height:1.55}
.col li::before{content:"";position:absolute;left:2px;top:5px;width:3px;height:3px;border-radius:50%;background:var(--burgundy)}
.job-date{color:var(--burgundy);font-weight:600;font-size:9px}
.job-title{font-weight:600;font-size:9.5px;line-height:1.3}
.job-text{font-size:8.5px;line-height:1.35}
.job-text a{color:var(--burgundy);font-weight:600}
.all-jobs{margin-top:10px;display:flex;align-items:center;gap:6px}
.all-jobs i{width:9px;height:9px;border-radius:50%;background:#222}
.contact-form{display:flex;flex-direction:column;gap:3px;width:156px}
.contact-form .field{height:14px;border:1px solid #cfcfcf;font-size:7px;color:#777;padding:2px 3px}
.contact-form .message{height:36px}
.contact-form .submit{margin-top:3px;width:40px;height:13px;background:var(--burgundy);color:var(--white);font-size:8px;font-weight:600;text-align:center;line-height:13px}
.bottom-rule{left:124px;top:1156px;width:745px;height:1px;background:var(--rule)}
.bottom-nav{left:124px;top:1174px;font-size:8.5px;color:#222;display:flex;gap:11px}
.bottom-nav a:first-child{color:var(--burgundy)}
.copyright{right:124px;top:1174px;font-size:8.5px;color:#222}
</style>
</head>
<body>

<header>
  <div class="abs brand"><span class="brand-mark"></span><span class="brand-name">Tallowmere Office Partners</span></div>
  <nav class="abs account">
    <a href="#"><span class="ico"></span>Login</a><span class="sep">|</span>
    <a href="#"><span class="ico"></span>Sign Up</a><span class="sep">|</span>
    <a href="#"><span class="ico"></span>Register</a>
  </nav>
  <div class="abs nav-rule" style="top:85px"></div>
  <nav class="abs main-nav">
    <a href="#">HOME</a><a href="#">ABOUT US</a><a href="#">CLIENTS</a><a href="#">SERVICES</a><a href="#">GALLERY</a><a href="#">CAREERS</a><a href="#">CONTACT US</a>
    <span class="social"><span></span><span></span><span></span></span>
  </nav>
  <div class="abs nav-rule" style="top:115px"></div>
</header>

<section>
  <div class="abs hero" role="img" aria-label="Dark monochrome photo of wine grape clusters"></div>
  <h1 class="abs hero-title">Etiam et tellus vel turpis</h1>
  <div class="abs hero-sub"><i></i>Nam quis ligula a nibh fermentum<i></i></div>

  <a class="abs action active" style="left:235px;top:311px" href="#">
    <div class="ring"><svg width="18" height="22" viewBox="0 0 18 22" fill="none" stroke="#fff" stroke-width="1.5"><path d="M2 1h9l5 5v15H2z"/><path d="M11 1v5h5"/><path d="M9 12v6M6 15h6"/></svg></div>
    Post Job<b>Vacancies</b></a>
  <a class="abs action" style="left:339px;top:311px" href="#">
    <div class="ring"><svg width="18" height="22" viewBox="0 0 18 22" fill="none" stroke="#fff" stroke-width="1.5"><rect x="2" y="3" width="14" height="18"/><rect x="6" y="1" width="6" height="4"/><path d="M5 10h8M5 13h8M5 16h8"/></svg></div>
    Review<b>Application</b></a>
  <a class="abs action" style="left:443px;top:311px" href="#">
    <div class="ring"><svg width="18" height="22" viewBox="0 0 18 22" fill="none" stroke="#fff" stroke-width="1.5"><path d="M2 1h9l5 5v15H2z"/><path d="M11 1v5h5"/><path d="M9 18v-7M6 14l3-3 3 3"/></svg></div>
    Upload<b>CV</b></a>

  <div class="abs photo" style="left:660px;top:130px;width:209px;height:206px" role="img" aria-label="Photo of a business team seated at a meeting table"></div>
  <div class="abs photo" style="left:660px;top:338px;width:209px;height:125px;background:linear-gradient(135deg,#c9ccd2,#6f7480)" role="img" aria-label="Photo of a businesswoman standing in a conference room"></div>

  <div class="abs divider"></div>
  <div class="abs divider-dot"></div>
</section>

<section>
  <h2 class="abs welcome-title">Welcome to <strong>Tallowmere Office Partners</strong></h2>
  <div class="abs circle" style="left:353px;background:linear-gradient(135deg,#f2f2f2,#9aa3ad)" role="img" aria-label="Photo of hands typing on a laptop"></div>
  <div class="abs circle" style="left:450px;background:linear-gradient(135deg,#6d7f4a,#3b1a22)" role="img" aria-label="Photo of a wine bottle, glass and grapes"></div>
  <div class="abs circle" style="left:545px;background:linear-gradient(135deg,#ececec,#8d8a86)" role="img" aria-label="Photo of a support team wearing headsets"></div>

  <div class="abs intro">
    <p>Welcome to Tallowmere Office Partners, an emerging provider of global IT consulting and software services. We are part of the Hollin Cellarworks group, a family run business and the world's largest multi-channel home delivery wine merchant operating in the UK, USA, Australia, Germany, Hong Kong, Poland and Switzerland.</p>
    <p>Mainly based in the rich cultural city of Chennai in the south east of India, Tallowmere Office Partners' vision is to deliver outstanding technology solutions to all of the Hollin Cellarworks' group companies that improve business processes, drive efficiencies, support rapid growth and elevate the overall customer experience to a different level.</p>
    <p class="lead">For further information about Hollin Cellarworks please visit <a href="#">www.hollincellarworks.example</a> or alternatively contact us.</p>
  </div>
</section>

<section>
  <div class="abs band" style="top:865px"></div>
  <div class="abs partners">
    <span>Brackwell Wine</span><span>Ledger Vine</span><span>Ostlers</span><span>Morrow Wine Circle</span><span>Hollin Cellarworks</span><span>Cask Folk</span><span>Verrand House</span>
  </div>
  <div class="abs band" style="top:953px"></div>
</section>

<footer>
  <div class="abs col" style="left:124px">
    <h3>About Us</h3>
    <ul><li>Our culture</li><li>The team</li></ul>
    <h3>Careers</h3>
    <ul><li>Current opportunities</li><li>Why join Tallowmere?</li><li>Application process</li></ul>
  </div>
  <div class="abs col" style="left:293px">
    <h3>Services</h3>
    <ul><li>Packaged Applications</li><li>Enterprise Application Integration</li><li>Digital Commerce</li><li>Application Development<br>&amp; Maintenance</li></ul>
  </div>
  <div class="abs col" style="left:492px;width:180px">
    <h3>Latest opportunities</h3>
    <div class="job-date">26/11/2013</div>
    <div class="job-title">Software Developers/Programmer Analysts - ERP</div>
    <div class="job-text">We are looking for a ERP Software Developer to join... <a href="#">read more</a></div>
    <div class="all-jobs"><i></i>See all current opportunities</div>
  </div>
  <div class="abs col" style="left:713px">
    <h3>Contact Us</h3>
    <form class="contact-form">
      <div class="field">Name</div>
      <div class="field">Email</div>
      <div class="field">Phone</div>
      <div class="field message">Message</div>
      <div class="submit">Submit</div>
    </form>
  </div>

  <div class="abs bottom-rule"></div>
  <nav class="abs bottom-nav"><a href="#">Home</a><a href="#">About us</a><a href="#">Clients</a><a href="#">Services</a><a href="#">Gallery</a><a href="#">Careers</a><a href="#">Contact Us</a></nav>
  <div class="abs copyright">© 2014 Copyright Tallowmere Office Partners Private Limited.</div>
</footer>

</body>
</html>
```